Vellora Labs - Mushroom Supplement Packaging

Our brand is called Vellora Labs. I've added a couple different logos that you can use. We are creating a line up of Mushroom Supplement products. I will add the entire line-up of products here. I've added examples of other products and packaging shape types I can purchase. Give me different options for packaging that is minimalist and clean for this brand that makes it look really well made and clean and make people want to buy.

Product 1 Lions Mane 1g
Product 2 Cordyceps 1g
Product 3 Chaga 1g
Product 4 Turkey Tail 1g
Product 5 Reishi 1g
Product 6 Maitake 1g
Product 7 Shiitake 1g

Product 8 (Mix) Lions Mane 143mg
Cordyceps 143mg
Chaga 143mg
Turkey Tail 143mg
Reishi 143mg
Maitake 143mg
Shiitake 143mg

```html
<!DOCTYPE html>
<html lang="en">
<head>
<meta charset="utf-8">
<title>Vellora Labs – Mushroom Brain Booster Labels</title>
<link rel="stylesheet" href="https://fonts.googleapis.com/css2?family=Montserrat:wght@400;500;600;700;800&display=swap">
<style>
  :root {
    --canvas: #ebebea;
    --ink: #1f1f21;
    --ink-soft: #35353a;
    --paper: #f2f2f1;
    --paper-edge: #d6d6d5;
    --title: #f3f1ee;

    --mix: #9c80a8;
    --turkey-tail: #e27e7b;
    --reishi: #d1685c;
    --shiitake: #d3ac5d;
    --maitake: #5e8f56;
    --chaga: #6e74a7;
    --lions-mane: #4e8aa9;
    --cordyceps: #c9714e;
  }

  * { box-sizing: border-box; margin: 0; padding: 0; }

  html, body {
    width: 1200px;
    height: 900px;
    overflow: hidden;
  }

  body {
    background: var(--canvas);
    font-family: "Montserrat", sans-serif;
    color: var(--ink);
  }

  .lineup {
    position: relative;
    width: 1200px;
    height: 900px;
  }

  .lineup__row {
    position: absolute;
    left: 168px;
    right: 168px;
    display: flex;
    justify-content: space-between;
    align-items: flex-start;
  }

  .lineup__row--top { top: 188px; }
  .lineup__row--bottom { top: 512px; }

  /* ---------- Label base ---------- */
  .label {
    display: flex;
    flex-direction: column;
    border-radius: 3px;
    overflow: hidden;
    box-shadow: 0 6px 14px rgba(0,0,0,.12);
    text-align: center;
    white-space: nowrap;
  }

  .label__band {
    background: linear-gradient(100deg, var(--tone) 0%, color-mix(in srgb, var(--tone) 76%, #000) 100%);
    display: flex;
    flex-direction: column;
    align-items: center;
    justify-content: center;
  }

  .label__brand {
    display: flex;
    align-items: center;
    font-weight: 800;
    text-transform: uppercase;
    letter-spacing: .06em;
    color: var(--ink);
  }

  .label__brand-dot {
    border-radius: 50%;
    background: var(--ink);
  }

  .label__name {
    font-weight: 800;
    color: var(--title);
    text-transform: uppercase;
  }

  .label__tagline {
    font-weight: 500;
    text-transform: uppercase;
    color: var(--ink-soft);
  }

  .label__info {
    flex: 1;
    background: linear-gradient(180deg, var(--paper) 0%, #ffffff 45%, var(--paper-edge) 100%);
    display: flex;
    flex-direction: column;
    align-items: center;
    justify-content: center;
  }

  .label__kicker {
    font-weight: 700;
    letter-spacing: .05em;
    text-transform: uppercase;
  }

  .label__benefit {
    font-weight: 500;
    letter-spacing: .03em;
  }

  .label__rule {
    width: 56%;
    height: 2px;
    background: var(--tone);
  }

  .label__count {
    font-weight: 700;
    letter-spacing: .1em;
    text-transform: uppercase;
  }

  .label__count-num {
    color: var(--tone);
    margin-right: .25em;
    font-size: 1.25em;
  }

  .label__type {
    font-weight: 500;
    letter-spacing: .12em;
    text-transform: uppercase;
  }

  /* ---------- Small jar label ---------- */
  .label--small { width: 160px; height: 124px; }
  .label--small .label__band { height: 72px; padding: 5px 6px; }
  .label--small .label__brand { font-size: 8px; line-height: 10px; gap: 3px; margin-bottom: 4px; }
  .label--small .label__brand-dot { width: 6px; height: 6px; }
  .label--small .label__name { font-size: 15px; line-height: 17px; letter-spacing: .05em; }
  .label--small .label__name--mix { font-size: 10px; line-height: 11px; letter-spacing: .08em; }
  .label--small .label__tagline { font-size: 6px; line-height: 8px; letter-spacing: .06em; margin-top: 3px; }
  .label--small .label__info { padding: 3px 6px; }
  .label--small .label__kicker { font-size: 6px; line-height: 8px; }
  .label--small .label__benefit { font-size: 6px; line-height: 8px; }
  .label--small .label__rule { width: 52%; height: 1px; margin: 5px 0 4px; }
  .label--small .label__count { font-size: 5px; line-height: 7px; }
  .label--small .label__type { font-size: 5px; line-height: 7px; }

  /* ---------- Large jar label ---------- */
  .label--large { width: 264px; height: 198px; margin-top: 3px; }
  .label--large .label__band { height: 122px; padding: 8px 10px; }
  .label--large .label__brand { font-size: 15px; line-height: 18px; gap: 6px; margin-bottom: 10px; }
  .label--large .label__brand-dot { width: 11px; height: 11px; }
  .label--large .label__name { font-size: 29px; line-height: 32px; letter-spacing: .06em; }
  .label--large .label__tagline { font-size: 10px; line-height: 13px; letter-spacing: .08em; margin-top: 6px; }
  .label--large .label__info { padding: 6px 10px; }
  .label--large .label__kicker { font-size: 10px; line-height: 13px; }
  .label--large .label__benefit { font-size: 10px; line-height: 13px; }
  .label--large .label__rule { margin: 8px 0 6px; }
  .label--large .label__count { font-size: 8px; line-height: 11px; }
  .label--large .label__type { font-size: 8px; line-height: 11px; }

  /* ---------- Featured jar label ---------- */
  .label--featured { width: 290px; height: 218px; margin-top: 0; }
  .label--featured .label__band { height: 134px; }
  .label--featured .label__brand { font-size: 16px; line-height: 19px; margin-bottom: 12px; }
  .label--featured .label__brand-dot { width: 12px; height: 12px; }
  .label--featured .label__name { font-size: 28px; line-height: 32px; letter-spacing: .06em; }
  .label--featured .label__tagline { font-size: 11px; line-height: 14px; }
  .label--featured .label__kicker { font-size: 10.5px; line-height: 14px; }
  .label--featured .label__benefit { font-size: 10.5px; line-height: 14px; }
  .label--featured .label__count { font-size: 8.5px; line-height: 12px; }
  .label--featured .label__type { font-size: 8.5px; line-height: 12px; }

  .label--mix { --tone: var(--mix); }
  .label--turkey-tail { --tone: var(--turkey-tail); }
  .label--reishi { --tone: var(--reishi); }
  .label--shiitake { --tone: var(--shiitake); }
  .label--maitake { --tone: var(--maitake); }
  .label--chaga { --tone: var(--chaga); }
  .label--lions-mane { --tone: var(--lions-mane); }
  .label--cordyceps { --tone: var(--cordyceps); }
</style>
</head>
<body>
<main class="lineup">

  <section class="lineup__row lineup__row--top">
    <article class="label label--small label--mix">
      <div class="label__band">
        <div class="label__brand"><span class="label__brand-dot"></span>Vellora Labs</div>
        <h2 class="label__name label__name--mix">(Mix)<br>Lion’s Mane</h2>
        <p class="label__tagline">Mushroom Brain Booster</p>
      </div>
      <div class="label__info">
        <p class="label__benefit">Cordyceps, Chaga, Turkey Tail</p>
        <p class="label__benefit">Reishi, Maitake, Shiitake</p>
        <span class="label__rule"></span>
        <p class="label__count"><span class="label__count-num">60</span>Capsules</p>
        <p class="label__type">Dietary Supplement</p>
      </div>
    </article>

    <article class="label label--small label--turkey-tail">
      <div class="label__band">
        <div class="label__brand"><span class="label__brand-dot"></span>Vellora Labs</div>
        <h2 class="label__name">Turkey Tail</h2>
        <p class="label__tagline">Mushroom Brain Booster</p>
      </div>
      <div class="label__info">
        <p class="label__kicker">Immunity Mushroom</p>
        <p class="label__benefit">Supercharge Your Health</p>
        <span class="label__rule"></span>
        <p class="label__count"><span class="label__count-num">60</span>Capsules</p>
        <p class="label__type">Dietary Supplement</p>
      </div>
    </article>

    <article class="label label--small label--reishi">
      <div class="label__band">
        <div class="label__brand"><span class="label__brand-dot"></span>Vellora Labs</div>
        <h2 class="label__name">Reishi</h2>
        <p class="label__tagline">Mushroom Brain Booster</p>
      </div>
      <div class="label__info">
        <p class="label__kicker">Immortality Mushroom</p>
        <p class="label__benefit">Vitality, Healthy Aging &amp; Longevity</p>
        <span class="label__rule"></span>
        <p class="label__count"><span class="label__count-num">60</span>Capsules</p>
        <p class="label__type">Dietary Supplement</p>
      </div>
    </article>

    <article class="label label--small label--shiitake">
      <div class="label__band">
        <div class="label__brand"><span class="label__brand-dot"></span>Vellora Labs</div>
        <h2 class="label__name">Shiitake</h2>
        <p class="label__tagline">Mushroom Brain Booster</p>
      </div>
      <div class="label__info">
        <p class="label__kicker">Energize Mushroom</p>
        <p class="label__benefit">Immune and Cellular Support</p>
        <span class="label__rule"></span>
        <p class="label__count"><span class="label__count-num">60</span>Capsules</p>
        <p class="label__type">Dietary Supplement</p>
      </div>
    </article>

    <article class="label label--small label--maitake">
      <div class="label__band">
        <div class="label__brand"><span class="label__brand-dot"></span>Vellora Labs</div>
        <h2 class="label__name">Maitake</h2>
        <p class="label__tagline">Mushroom Brain Booster</p>
      </div>
      <div class="label__info">
        <p class="label__kicker">Immunity Mushroom</p>
        <p class="label__benefit">Support Your Health Heart</p>
        <span class="label__rule"></span>
        <p class="label__count"><span class="label__count-num">60</span>Capsules</p>
        <p class="label__type">Dietary Supplement</p>
      </div>
    </article>
  </section>

  <section class="lineup__row lineup__row--bottom">
    <article class="label label--large label--chaga">
      <div class="label__band">
        <div class="label__brand"><span class="label__brand-dot"></span>Vellora Labs</div>
        <h2 class="label__name">Chaga</h2>
        <p class="label__tagline">Mushroom Brain Booster</p>
      </div>
      <div class="label__info">
        <p class="label__kicker">Vitality Mushroom</p>
        <p class="label__benefit">Rejuvenate Your Body</p>
        <span class="label__rule"></span>
        <p class="label__count"><span class="label__count-num">60</span>Capsules</p>
        <p class="label__type">Dietary Supplement</p>
      </div>
    </article>

    <article class="label label--large label--featured label--lions-mane">
      <div class="label__band">
        <div class="label__brand"><span class="label__brand-dot"></span>Vellora Labs</div>
        <h2 class="label__name">Lion’s Mane</h2>
        <p class="label__tagline">Mushroom Brain Booster</p>
      </div>
      <div class="label__info">
        <p class="label__kicker">Smart Mushroom</p>
        <p class="label__benefit">Improve Your Focus</p>
        <span class="label__rule"></span>
        <p class="label__count"><span class="label__count-num">60</span>Capsules</p>
        <p class="label__type">Dietary Supplement</p>
      </div>
    </article>

    <article class="label label--large label--cordyceps">
      <div class="label__band">
        <div class="label__brand"><span class="label__brand-dot"></span>Vellora Labs</div>
        <h2 class="label__name">Cordyceps</h2>
        <p class="label__tagline">Mushroom Brain Booster</p>
      </div>
      <div class="label__info">
        <p class="label__kicker">Endurance Mushroom</p>
        <p class="label__benefit">Boost Your Energy</p>
        <span class="label__rule"></span>
        <p class="label__count"><span class="label__count-num">60</span>Capsules</p>
        <p class="label__type">Dietary Supplement</p>
      </div>
    </article>
  </section>

</main>
</body>
</html>
```